EASY Design some Business Cards

Black and white business cards needed for photographer. see instructions attached. Please make sure files are printable! Logo is also attached

```html
<!DOCTYPE html>
<html lang="en">
<head>
<meta charset="utf-8">
<title>Hold Steady Photography – Business Cards</title>
<link href="https://fonts.googleapis.com/css2?family=Roboto:wght@400;700;900&display=swap" rel="stylesheet">
<style>
  :root {
    --ink: #0d0d0d;
    --paper: #ffffff;
    --stage: #cfcfcf;
    --muted: #d9d9d9;
  }
  * { box-sizing: border-box; margin: 0; padding: 0; }
  html, body { width: 1200px; height: 900px; overflow: hidden; }
  body {
    background: var(--stage);
    font-family: "Roboto", Arial, sans-serif;
    position: relative;
  }
  .card {
    position: absolute;
    width: 520px;
    height: 300px;
    border-radius: 26px;
    overflow: hidden;
  }
  .card--front { left: 70px; top: 470px; background: var(--ink); }
  .card--back { left: 610px; top: 130px; background: var(--paper); }

  .back-shape { position: absolute; inset: 0; }

  .brand {
    position: absolute;
    display: flex;
    flex-direction: column;
    align-items: center;
    font-weight: 900;
    text-transform: uppercase;
    text-align: center;
  }
  .brand__dot { border-radius: 50%; margin-bottom: 14px; }
  .brand__name { letter-spacing: 1px; line-height: 1.15; }

  .card--front .brand { left: 0; right: 0; top: 40px; color: var(--paper); }
  .card--front .brand__dot { width: 120px; height: 120px; background: var(--paper); }
  .card--front .brand__name { font-size: 26px; }
  .card--front .brand__sub { font-size: 26px; letter-spacing: 6px; }

  .card--back .brand { right: 30px; top: 118px; width: 210px; color: var(--ink); }
  .card--back .brand__dot { width: 96px; height: 96px; background: var(--ink); margin-bottom: 10px; }
  .card--back .brand__name { font-size: 20px; }
  .card--back .brand__sub { font-size: 20px; letter-spacing: 5px; }

  .identity { position: absolute; left: 30px; top: 22px; color: var(--paper); }
  .identity__name { font-size: 20px; font-weight: 700; }
  .identity__role { font-size: 13px; font-weight: 700; color: var(--muted); }

  .contacts { position: absolute; left: 30px; top: 80px; list-style: none; color: var(--paper); }
  .contacts li { display: flex; align-items: center; gap: 8px; height: 23px; font-size: 12px; }
  .icon {
    width: 16px; height: 16px; border-radius: 50%;
    border: 1.4px solid var(--paper);
    display: flex; align-items: center; justify-content: center;
    flex: none;
  }
  .icon svg { width: 9px; height: 9px; }
</style>
</head>
<body>

<section class="card card--front" aria-label="Card front">
  <div class="brand">
    <span class="brand__dot"></span>
    <span class="brand__name">Hold Steady</span>
    <span class="brand__sub">Photography</span>
  </div>
</section>

<section class="card card--back" aria-label="Card back">
  <svg class="back-shape" viewBox="0 0 520 300" preserveAspectRatio="none" aria-hidden="true">
    <path d="M0 0 H370 C335 55 265 70 215 130 C170 185 185 255 160 300 H0 Z" fill="#0d0d0d"/>
  </svg>

  <div class="identity">
    <p class="identity__name">Dorian Ellis</p>
    <p class="identity__role">Photographer</p>
  </div>

  <ul class="contacts">
    <li><span class="icon"><svg viewBox="0 0 10 10"><path d="M2 1 L4 1 L4.5 3 L3.3 3.8 C3.8 5 5 6.2 6.2 6.7 L7 5.5 L9 6 L9 8 C5 8.5 1.5 5 2 1 Z" fill="#fff"/></svg></span>555-014-2290</li>
    <li><span class="icon"><svg viewBox="0 0 10 10"><rect x="1" y="2.5" width="8" height="5.5" fill="none" stroke="#fff" stroke-width="1"/><path d="M1 2.5 L5 5.5 L9 2.5" fill="none" stroke="#fff" stroke-width="1"/></svg></span>HSPstudio.com</li>
    <li><span class="icon"></span>www.HSPstudio.com</li>
    <li><span class="icon"><svg viewBox="0 0 10 10"><path d="M5 9.5 C2.5 6.5 2 5 2 4 A3 3 0 0 1 8 4 C8 5 7.5 6.5 5 9.5 Z" fill="#fff"/><circle cx="5" cy="4" r="1.1" fill="#0d0d0d"/></svg></span>14 Alder Rd Ferndale NSW 2000</li>
    <li><span class="icon"></span>Dorian Ellis Photography</li>
    <li><span class="icon"></span>HSPstudio</li>
  </ul>

  <div class="brand">
    <span class="brand__dot"></span>
    <span class="brand__name">Hold Steady</span>
    <span class="brand__sub">Photography</span>
  </div>
</section>

</body>
</html>
```